Sunscreen Package Design Modern SPF 50

Update current package design to a more modern design target women 16-40 Do not make it playful. DUNE HAVEN is home to movie stars and high income business people PalmSprings is one of the most desired vacation areas in the world. The sun shines 350 days a year. World class Tennis and Golf tournaments are held every year with the worlds top players attending these tournaments

Target Market(s)

Women

Industry/Entity Type

Skin Protection

Font styles to use
Sans Serif

Requirements
Must have
• The words DUNE HAVEN and VELORIMA

```html
<!DOCTYPE html>
<html lang="en">
<head>
<meta charset="utf-8">
<title>Dune Haven Velorima – Sunscreen &amp; Aftersun</title>
<link rel="stylesheet" href="https://fonts.googleapis.com/css2?family=Cormorant+Garamond:wght@500&family=Montserrat:wght@400;500&display=swap">
<style>
  :root{
    --bg-top:#ececec;
    --bg-bottom:#dcdcdc;
    --cream:#ddd3c5;
    --cream-shade:#cfc4b4;
    --terracotta:#b8694a;
    --cap-terracotta:#b26a4c;
    --cap-terracotta-edge:#9c5a3f;
    --ink:#3b302a;
    --sage:#8f9b87;
    --sage-shade:#7f8b78;
    --cap-green:#4f5b3e;
    --cap-green-edge:#3f4a31;
    --leaf:#6f7c67;
    --ivory:#f3f1ea;
  }
  *{margin:0;padding:0;box-sizing:border-box}
  html,body{width:1200px;height:912px;overflow:hidden}
  body{
    position:relative;
    background:linear-gradient(180deg,var(--bg-top),var(--bg-bottom));
    font-family:"Montserrat",sans-serif;
  }
  .tubes{position:absolute;inset:0}
  .label{position:absolute;left:0;top:0;width:1200px;height:912px}
  .t{position:absolute;transform:translate(-50%,-50%);white-space:nowrap;text-align:center;line-height:1}
  .brand{font-family:"Montserrat",sans-serif;font-weight:400;font-size:34px;letter-spacing:4px;padding-left:4px}
  .maker{font-size:10.5px;letter-spacing:3.6px;font-weight:500;padding-left:3.6px}
  .product{font-size:11px;letter-spacing:4px;font-weight:500;padding-left:4px}
  .claim{font-size:9.5px;letter-spacing:.2px}
  .claim.wide{letter-spacing:1.4px}
  .size{font-size:10px}
  .sunscreen .t{color:var(--ink)}
  .sunscreen .spf{font-size:15px;font-weight:500;color:var(--terracotta)}
  .sunscreen .spf-num{font-family:"Cormorant Garamond",serif;font-size:50px;font-weight:500;color:var(--terracotta);font-variant-numeric:lining-nums}
  .aftersun .t{color:var(--ivory)}
  .aftersun .product{letter-spacing:4.5px;font-size:12px;padding-left:4.5px}
  .brand-dot{position:absolute}
</style>
</head>
<body>
  <svg class="tubes" width="1200" height="912" viewBox="0 0 1200 912" aria-hidden="true">
    <defs>
      <linearGradient id="creamBody" x1="0" x2="1">
        <stop offset="0" stop-color="#cfc4b4"/>
        <stop offset=".45" stop-color="#ddd3c5"/>
        <stop offset="1" stop-color="#cfc4b4"/>
      </linearGradient>
      <linearGradient id="sageBody" x1="0" x2="1">
        <stop offset="0" stop-color="#7f8b78"/>
        <stop offset=".5" stop-color="#8f9b87"/>
        <stop offset="1" stop-color="#7f8b78"/>
      </linearGradient>
    </defs>
    <path class="tube-body" d="M280 92 H579 Q572 420 528 735 H345 Q296 420 280 92 Z" fill="url(#creamBody)"/>
    <rect class="tube-cap" x="345" y="735" width="183" height="98" rx="8" fill="#b26a4c"/>
    <rect class="cap-hinge" x="409" y="780" width="55" height="34" rx="2" fill="none" stroke="#9c5a3f" stroke-width="2"/>
    <path class="tube-body" d="M641 93 H942 Q934 420 877 735 H709 Q652 420 641 93 Z" fill="url(#sageBody)"/>
    <rect class="tube-cap" x="709" y="733" width="168" height="97" rx="8" fill="#4f5b3e"/>
    <rect class="cap-hinge" x="767" y="775" width="52" height="34" rx="2" fill="none" stroke="#3f4a31" stroke-width="2"/>
    <line class="rule" x1="426" y1="360" x2="426" y2="456" stroke="#3b302a" stroke-width="1.2"/>
    <line class="rule" x1="801" y1="403" x2="801" y2="514" stroke="#f3f1ea" stroke-width="1.2"/>
  </svg>

  <section class="label sunscreen">
    <svg class="brand-dot" style="left:410px;top:182px" width="32" height="32" viewBox="0 0 32 32" aria-hidden="true">
      <circle cx="16" cy="16" r="16" fill="#b8694a"/>
    </svg>
    <div class="t brand" style="left:426px;top:258px">DUNE</div>
    <div class="t brand" style="left:426px;top:298px">HAVEN</div>
    <div class="t maker" style="left:426px;top:332px">VELORIMA<sup style="font-size:5px">®</sup></div>
    <div class="t product" style="left:426px;top:491px">SUNSCREEN</div>
    <div class="t spf" style="left:425px;top:524px">SPF</div>
    <div class="t spf-num" style="left:425px;top:557px">50</div>
    <div class="t claim" style="left:425px;top:599px">UVA + UVB PROTECTION</div>
    <div class="t claim wide" style="left:425px;top:616px">BROAD SPECTRUM</div>
    <div class="t claim" style="left:425px;top:635px">WATER RESISTANT (80 MINUTES)</div>
    <div class="t size" style="left:424px;top:692px">3 FL OZ / 88 mL</div>
  </section>

  <section class="label aftersun">
    <svg class="brand-dot" style="left:786px;top:212px" width="30" height="30" viewBox="0 0 30 30" aria-hidden="true">
      <rect width="30" height="30" fill="#6f7c67"/>
    </svg>
    <div class="t brand" style="left:800px;top:289px">DUNE</div>
    <div class="t brand" style="left:800px;top:328px">HAVEN</div>
    <div class="t maker" style="left:800px;top:362px">VELORIMA<sup style="font-size:5px">®</sup></div>
    <div class="t product" style="left:800px;top:555px">AFTERSUN</div>
    <div class="t claim" style="left:800px;top:593px">HYDRATE / SOOTHE / RESTORE</div>
    <div class="t claim" style="left:800px;top:617px">WITH ALOE, HYALURONATE ACID</div>
    <div class="t claim" style="left:800px;top:635px">CUCUMBER &amp; JOJOBA</div>
    <div class="t size" style="left:800px;top:686px">3 FL OZ / 88 mL</div>
  </section>
</body>
</html>
```